“Fleet Vehicle Branding: Truck Wrap for Harbor Climate & Air”

The C in custom must be the same as in the logo tan and blue image
the logo .jpg need to have that same C. are colors are Tan and navy blue not sure how we weather we want most the truck tan or blue with some of these things from logos. also are saying is harbor warmth harbor trust harbor climate and air. we would like to stand out from traditional hvac wrap looks

Target Market(s)

Residential Customers

Industry/Entity Type

Hvac

Colors

Designer to choose colors to be used in the design.

Requirements
Must have
• TACLB008315R
Nice to have
• www.harborclimate-air-example.com

```html
<!DOCTYPE html>
<html lang="en">
<head>
<meta charset="utf-8">
<title>Harbor Climate &amp; Air — Fleet Wrap</title>
<link rel="stylesheet" href="https://fonts.googleapis.com/css2?family=Heebo:wght@400;700&family=Roboto+Condensed:wght@700&display=swap">
<style>
  :root {
    --tan-light: #e6d3b3;
    --tan-dark: #c3a780;
    --navy: #0f2552;
    --navy-deep: #0a1b3f;
    --logo-blue: #24467a;
    --web-tan: #c8b08a;
    --white: #ffffff;
    --trim: #1e1f24;
    --glass-top: #8d8e93;
    --glass-bottom: #b9babd;
    --hub: #cfd0d3;
    --tail: #c4303a;
    --amber: #f0a629;
    --backdrop: #f4f4f6;
  }
  * { margin: 0; padding: 0; box-sizing: border-box; }
  html, body { width: 1200px; height: 720px; overflow: hidden; background: var(--backdrop); }
  .canvas { position: relative; width: 1200px; height: 720px; }
  .vehicle { position: absolute; left: 0; top: 0; }
  .centered { position: absolute; transform: translateX(-50%); white-space: nowrap; text-align: center; }

  .emblem-name {
    left: 279px; top: 226px;
    font-family: "Heebo", sans-serif; font-weight: 700; font-size: 27px; line-height: 1.15;
    color: var(--white);
  }
  .door-name {
    left: 532px; top: 176px;
    font-family: "Heebo", sans-serif; font-weight: 700; font-size: 22px;
    color: var(--logo-blue);
  }
  .services {
    left: 532px; top: 212px;
    font-family: "Roboto Condensed", sans-serif; font-weight: 700; font-size: 14px;
    color: var(--navy);
  }
  .phone {
    left: 532px; top: 225px;
    font-family: "Roboto Condensed", sans-serif; font-weight: 700; font-size: 33px; line-height: 1.1;
    color: var(--navy);
  }
  .tagline {
    left: 532px; top: 260px;
    font-family: "Heebo", sans-serif; font-weight: 700; font-size: 22px;
    color: var(--navy);
  }
  .license {
    left: 532px; top: 297px;
    font-family: "Heebo", sans-serif; font-weight: 700; font-size: 23px;
    color: var(--navy);
  }
  .side-name { left: 686px; top: 372px; color: var(--white); }
  .side-name__word { display: block; font-family: "Heebo", sans-serif; font-weight: 700; font-size: 41px; line-height: 1.1; }
  .side-name__line { display: block; font-family: "Heebo", sans-serif; font-weight: 400; font-size: 31px; line-height: 1.1; }
  .website {
    left: 637px; top: 478px;
    font-family: "Heebo", sans-serif; font-weight: 400; font-size: 18px;
    color: var(--web-tan); letter-spacing: 0.3px;
  }
</style>
</head>
<body>
<main class="canvas">
  <svg class="vehicle" width="1200" height="720" viewBox="0 0 1200 720">
    <defs>
      <linearGradient id="tanShade" x1="0" y1="0" x2="0" y2="1">
        <stop offset="0" stop-color="var(--tan-light)"/>
        <stop offset="1" stop-color="var(--tan-dark)"/>
      </linearGradient>
      <linearGradient id="glassShade" x1="0" y1="0" x2="0" y2="1">
        <stop offset="0" stop-color="var(--glass-top)"/>
        <stop offset="1" stop-color="var(--glass-bottom)"/>
      </linearGradient>
      <clipPath id="bodyClip">
        <path d="M85,520 L85,300 L135,145 Q140,131 160,131 L800,137 Q845,141 865,165 L990,300 L1081,316 Q1122,330 1125,352 L1125,520 L1066,520 A94,94 0 0 0 878,520 L393,520 A94,94 0 0 0 205,520 Z"/>
      </clipPath>
    </defs>

    <ellipse class="vehicle__shadow" cx="600" cy="586" rx="540" ry="6" fill="#d6d6da"/>

    <g clip-path="url(#bodyClip)">
      <rect class="vehicle__paint" x="80" y="125" width="1060" height="410" fill="url(#tanShade)"/>
      <path class="vehicle__swoosh" d="M380,540 Q560,400 780,350 Q940,318 1140,318 L1140,540 Z" fill="var(--navy-deep)"/>
      <rect class="vehicle__rear-pillar" x="80" y="130" width="60" height="90" fill="var(--trim)"/>
    </g>

    <polygon class="vehicle__window" role="img" aria-label="Cab side window" points="707,163 792,168 940,304 722,300 710,285" fill="url(#glassShade)" stroke="var(--trim)" stroke-width="5"/>
    <rect class="vehicle__tail-light" role="img" aria-label="Tail light" x="88" y="218" width="38" height="74" rx="4" fill="var(--tail)"/>
    <rect class="vehicle__headlight" role="img" aria-label="Headlight" x="1057" y="351" width="54" height="47" rx="8" fill="var(--amber)"/>
    <rect class="vehicle__rear-bumper" x="57" y="463" width="60" height="54" rx="5" fill="var(--trim)"/>
    <rect class="vehicle__front-bumper" x="1038" y="430" width="106" height="86" rx="6" fill="var(--trim)"/>

    <g class="vehicle__wheel" role="img" aria-label="Rear wheel">
      <circle cx="299" cy="509" r="80" fill="var(--trim)"/>
      <circle cx="299" cy="509" r="52" fill="var(--hub)"/>
    </g>
    <g class="vehicle__wheel" role="img" aria-label="Front wheel">
      <circle cx="972" cy="509" r="80" fill="var(--trim)"/>
      <circle cx="972" cy="509" r="52" fill="var(--hub)"/>
    </g>

    <circle class="vehicle__emblem" cx="279" cy="263" r="106" fill="var(--navy)"/>
  </svg>

  <div class="centered emblem-name">Harbor<br>Climate &amp; Air</div>

  <div class="centered door-name">Harbor Climate &amp; Air</div>
  <div class="centered services">HEATING • AIR CONDITIONING</div>
  <div class="centered phone">555-010-4827</div>
  <div class="centered tagline">HARBOR TRUST</div>
  <div class="centered license">TACLB008315R</div>

  <div class="centered side-name">
    <span class="side-name__word">HARBOR</span>
    <span class="side-name__line">Climate and Air</span>
  </div>
  <div class="centered website">WWW.HARBORCLIMATE-AIR-EXAMPLE.COM</div>
</main>
</body>
</html>
```